Stationery Design Project - KORVELT-NINE

Presentation Folder
Size: A4
Notepad
Size: 250mm x 140mm
With Compliments Slip
Size: DL
210mm x 99mm
Letterhead
Size: A4 - 210mm x 297mm
Business Cards
Size: 90mm x 55mm

Company is called "KORVELT-NINE"
website: www.korveltnine.com.au (under construction)

Offices: *Perth *Brisbane *Seoul *Hong Kong

If you need any further information please let me know!

Cheers

Lionel

```html
<!DOCTYPE html>
<html lang="en">
<head>
<meta charset="utf-8">
<title>KORVELT-NINE Notepad</title>
<link rel="stylesheet" href="https://fonts.googleapis.com/css2?family=Open+Sans:wght@300;400;600&display=swap">
<style>
  :root {
    --backdrop: #ececec;
    --paper: #ffffff;
    --blue-light: #0a9ee0;
    --blue-mid: #0866b4;
    --blue-deep: #061f5e;
    --silver: #b8babd;
    --silver-light: #f4f4f4;
    --logo-grey: #8a8d92;
    --rule: #9a9a9a;
  }
  * { box-sizing: border-box; margin: 0; padding: 0; }
  html, body { width: 1200px; height: 846px; overflow: hidden; }
  body {
    background: var(--backdrop);
    font-family: "Open Sans", Arial, sans-serif;
    position: relative;
  }
  .pad {
    position: absolute;
    top: 137px;
    width: 333px;
    height: 592px;
    overflow: hidden;
    background: var(--paper);
  }
  .pad--back { left: 52px; }
  .pad--front { left: 442px; background: linear-gradient(90deg, #dcdcdc 0%, var(--silver-light) 30%, #ffffff 60%, #e8e8e8 100%); }
  .pad--page { left: 816px; }

  /* back cover */
  .back-field {
    position: absolute; inset: 0;
    background: linear-gradient(180deg, var(--blue-light) 0%, var(--blue-mid) 38%, #07398a 68%, var(--blue-deep) 100%);
  }
  .contact {
    position: absolute; left: 30px; top: 500px;
    color: #fff; font-size: 8.5px; line-height: 12px; font-weight: 400;
  }
  .contact__address { margin-bottom: 6px; }
  .contact__row { display: flex; align-items: center; gap: 6px; }
  .contact__row svg { width: 8px; height: 8px; flex: none; }

  /* logo */
  .brand { position: absolute; display: flex; align-items: center; gap: 10px; }
  .brand__mark { background: var(--blue-light); flex: none; }
  .brand__name { font-weight: 300; color: var(--logo-grey); letter-spacing: 1px; }
  .pad--front .brand { left: 49px; top: 86px; }
  .pad--front .brand__mark { width: 58px; height: 58px; }
  .pad--front .brand__name { font-size: 26px; }
  .pad--page .brand { left: 16px; top: 62px; gap: 6px; }
  .pad--page .brand__mark { width: 34px; height: 34px; }
  .pad--page .brand__name { font-size: 15px; }

  /* photo grid */
  .gallery { position: absolute; left: 49px; top: 182px; display: grid; grid-template-columns: 112px 112px; grid-auto-rows: 79px; gap: 14px 14px; }
  .gallery__item { display: block; }
  .gallery__item--mining { background: linear-gradient(180deg, #5d8fc8 0%, #8a6a3e 60%, #7a3a1a 100%); }
  .gallery__item--wind { background: linear-gradient(180deg, #9aaac9 0%, #c9d2e2 50%, #4b6088 100%); }
  .gallery__item--offshore { background: linear-gradient(180deg, #1d3d66 0%, #2b4e78 60%, #1a3152 100%); }
  .gallery__item--tanker { background: linear-gradient(180deg, #273f62 0%, #4d6079 55%, #203656 100%); }

  .wave { position: absolute; left: 0; top: 0; width: 333px; height: 592px; }
  .offices {
    position: absolute; left: 0; right: 0; top: 516px;
    text-align: center; color: #fff; font-size: 11px; font-weight: 600; letter-spacing: 1px;
  }
  .website {
    position: absolute; left: 0; right: 0; top: 536px;
    text-align: center; color: #fff; font-size: 12px; font-weight: 600; letter-spacing: 1.5px;
  }
  .rules { position: absolute; left: 0; top: 0; }
</style>
</head>
<body>

  <section class="pad pad--back" aria-label="Notepad back cover">
    <div class="back-field" role="img" aria-label="Blue background of stacked three-dimensional blocks"></div>
    <div class="contact">
      <p class="contact__address">47 Marlow Street, Westhaven<br>Western Australia 6011</p>
      <p class="contact__row">
        <svg viewBox="0 0 10 10"><path d="M2 1h2l1 2-1 1a5 5 0 0 0 2 2l1-1 2 1v2c0 1-1 1-1 1A8 8 0 0 1 1 2s0-1 1-1z" fill="#fff"/></svg>
        08 5550 1427
      </p>
      <p class="contact__row">
        <svg viewBox="0 0 10 10"><circle cx="5" cy="5" r="4.2" fill="none" stroke="#fff" stroke-width="1"/><circle cx="5" cy="5" r="1.6" fill="none" stroke="#fff" stroke-width="1"/></svg>
        info@korveltnine.com.au
      </p>
      <p class="contact__row">
        <svg viewBox="0 0 10 10"><circle cx="5" cy="5" r="4.2" fill="none" stroke="#fff" stroke-width="1"/><path d="M1 5h8M5 1c-2 2-2 6 0 8M5 1c2 2 2 6 0 8" fill="none" stroke="#fff" stroke-width=".8"/></svg>
        www.korveltnine.com.au
      </p>
    </div>
  </section>

  <section class="pad pad--front" aria-label="Notepad front cover">
    <div class="brand">
      <span class="brand__mark"></span>
      <span class="brand__name">korvelt-nine</span>
    </div>
    <div class="gallery">
      <span class="gallery__item gallery__item--mining" role="img" aria-label="Photo of a bucket-wheel reclaimer at a mine site"></span>
      <span class="gallery__item gallery__item--wind" role="img" aria-label="Photo of an offshore wind turbine"></span>
      <span class="gallery__item gallery__item--offshore" role="img" aria-label="Photo of an offshore oil platform at sea"></span>
      <span class="gallery__item gallery__item--tanker" role="img" aria-label="Photo of an LNG tanker ship at sea"></span>
    </div>
    <svg class="wave" viewBox="0 0 333 592" aria-hidden="true">
      <defs>
        <linearGradient id="wave-blue" x1="0" y1="0" x2="0" y2="1">
          <stop offset="0" stop-color="#0a58a8"/>
          <stop offset=".5" stop-color="#0a8fd6"/>
          <stop offset="1" stop-color="#08408e"/>
        </linearGradient>
        <linearGradient id="wave-silver" x1="0" y1="0" x2="1" y2="0">
          <stop offset="0" stop-color="#9a9c9f"/>
          <stop offset=".6" stop-color="#c9cbcd"/>
          <stop offset="1" stop-color="#8d8f92"/>
        </linearGradient>
      </defs>
      <path d="M0 490 Q130 400 333 372 L333 592 L0 592 Z" fill="url(#wave-silver)"/>
      <path d="M0 502 Q140 412 333 382 L333 592 L0 592 Z" fill="url(#wave-blue)" role="img" aria-label="Blue block-pattern band"/>
    </svg>
    <p class="offices">*Perth *Brisbane *Seoul *Hong Kong</p>
    <p class="website">www.korveltnine.com.au</p>
  </section>

  <section class="pad pad--page" aria-label="Notepad writing page">
    <svg class="rules" width="333" height="592" viewBox="0 0 333 592" aria-hidden="true">
      <g stroke="var(--rule)" stroke-width=".8" stroke-dasharray="3 2">
        <line x1="172" y1="64" x2="306" y2="64"/>
        <line x1="172" y1="91.4" x2="306" y2="91.4"/>
        <line x1="22" y1="118.8" x2="306" y2="118.8"/>
        <line x1="22" y1="146.2" x2="306" y2="146.2"/>
        <line x1="22" y1="173.6" x2="306" y2="173.6"/>
        <line x1="22" y1="201" x2="306" y2="201"/>
        <line x1="22" y1="228.4" x2="306" y2="228.4"/>
        <line x1="22" y1="255.8" x2="306" y2="255.8"/>
        <line x1="22" y1="283.2" x2="306" y2="283.2"/>
        <line x1="22" y1="310.6" x2="306" y2="310.6"/>
        <line x1="22" y1="338" x2="306" y2="338"/>
        <line x1="22" y1="365.4" x2="306" y2="365.4"/>
        <line x1="22" y1="392.8" x2="306" y2="392.8"/>
        <line x1="22" y1="420.2" x2="306" y2="420.2"/>
        <line x1="22" y1="447.6" x2="306" y2="447.6"/>
        <line x1="22" y1="475" x2="306" y2="475"/>
        <line x1="22" y1="502.4" x2="306" y2="502.4"/>
        <line x1="22" y1="529.8" x2="306" y2="529.8"/>
        <line x1="22" y1="557.2" x2="306" y2="557.2"/>
      </g>
    </svg>
    <div class="brand">
      <span class="brand__mark"></span>
      <span class="brand__name">korvelt-nine</span>
    </div>
  </section>

</body>
</html>
```